Maple Hollow Bloom Panels Business card

Looking to have a business card design incorporating my logo for my flower wall business.

Industry/Entity Type

Wedding & event planning

Contact Information for Business Card

My business logo, my name - Lena Whitcombe (owner), my tagline - let us be your finishing touch, phone # 401-726-3148, email address - maplehollowbloompanels@mailvane.net, my website - maplehollowbloompanels.net, Instagram handle- @maplehollowbloompanels, FB handle Handle - maplehollowbloompanels

Font styles to use
Other font styles liked:
• Sentaina is the font that is used in my logo

Requirements
Must have
• Would like a double sided business card

```html
<!DOCTYPE html>
<html lang="en">
<head>
<meta charset="UTF-8">
<title>Maple Hollow Bloom Panels – Business Card</title>
<link rel="stylesheet" href="https://fonts.googleapis.com/css2?family=Tinos:ital@0;1&family=Allura&display=swap">
<style>
  :root {
    --canvas-bg: #ead5d9;
    --card-white: #ffffff;
    --card-soft: #f4f1f2;
    --blush: #f1c9d4;
    --blush-deep: #ebb9c7;
    --rose: #df6f96;
    --rose-band: #e0749a;
    --ink: #2a2a2a;
    --shadow: rgba(120, 70, 85, 0.22);
  }
  * { box-sizing: border-box; margin: 0; padding: 0; }
  html, body {
    width: 1200px; height: 1000px; overflow: hidden;
    background: var(--canvas-bg);
  }
  .canvas {
    position: relative; width: 1200px; height: 1000px;
    display: flex; align-items: center; justify-content: center; gap: 60px;
  }
  .card {
    position: relative; width: 520px; height: 297px; overflow: hidden;
    box-shadow: 0 10px 24px var(--shadow);
  }

  /* Back side */
  .card-back { background: var(--card-white); }
  .card-back .pattern-field {
    position: absolute; left: 20px; top: 18px; right: 20px; bottom: 18px;
    background: linear-gradient(135deg, var(--blush) 0%, var(--blush-deep) 100%);
  }
  .card-back .logo-panel {
    position: absolute; left: 137px; top: 0; width: 249px; height: 208px;
    background: var(--rose);
    display: flex; align-items: center; justify-content: center;
  }
  .logo-badge {
    width: 112px; height: 112px; border-radius: 50%;
    background: var(--card-soft);
    display: flex; align-items: center; justify-content: center; text-align: center;
    font-family: "Tinos", serif; font-size: 13px; line-height: 1.25;
    color: var(--ink); padding: 10px; letter-spacing: 0.5px;
  }
  .card-back .web-strip {
    position: absolute; left: 137px; top: 248px; width: 249px; height: 31px;
    background: var(--card-white);
    display: flex; align-items: center; justify-content: center;
    font-family: "Tinos", serif; font-size: 13.5px; letter-spacing: 0.6px; color: var(--ink);
  }

  /* Front side */
  .card-front { background: var(--card-soft); }
  .card-front .pattern-field {
    position: absolute; inset: 0;
    background: linear-gradient(135deg, #f6f3f4 0%, #f1e7ea 100%);
  }
  .card-front .brand-name {
    position: absolute; top: 42px; left: 0; right: 0; text-align: center;
    font-family: "Tinos", serif; font-size: 22px; letter-spacing: 1px; color: var(--ink);
  }
  .card-front .tagline-band {
    position: absolute; left: 0; right: 0; top: 107px; height: 27px;
    background: var(--rose-band);
    display: flex; align-items: center; justify-content: center;
    font-family: "Tinos", serif; font-style: italic; font-size: 13px;
    letter-spacing: 1.6px; color: var(--card-white);
  }
  .card-front .owner-name {
    position: absolute; top: 146px; left: 0; right: 0; text-align: center;
    font-family: "Allura", cursive; font-size: 50px; line-height: 60px; color: var(--rose);
  }
  .card-front .contact-line {
    position: absolute; top: 224px; left: 0; right: 0; text-align: center;
    font-family: "Tinos", serif; font-size: 13px; letter-spacing: 0.5px; color: var(--ink);
  }
  .contact-line .divider { margin: 0 6px; }
  .card-front .social-line {
    position: absolute; top: 248px; left: 0; right: 0;
    display: flex; align-items: center; justify-content: center; gap: 7px;
    font-family: "Tinos", serif; font-size: 13px; letter-spacing: 0.5px; color: var(--ink);
  }
  .social-dot { width: 13px; height: 13px; border-radius: 50%; background: var(--rose); }
</style>
</head>
<body>
<main class="canvas">
  <section class="card card-back" aria-label="Business card back">
    <div class="pattern-field" role="img" aria-label="Soft pink leaf and berry pattern"></div>
    <div class="logo-panel">
      <div class="logo-badge">Maple Hollow Bloom Panels</div>
    </div>
    <div class="web-strip">maplehollowbloompanels.net</div>
  </section>

  <section class="card card-front" aria-label="Business card front">
    <div class="pattern-field" role="img" aria-label="Faint pale leaf pattern"></div>
    <div class="brand-name">Maple Hollow Bloom Panels</div>
    <div class="tagline-band">let us be your finishing touch</div>
    <div class="owner-name">Lena Whitcombe</div>
    <div class="contact-line">401-726-3148<span class="divider">|</span>maplehollowbloompanels@mailvane.net</div>
    <div class="social-line"><span class="social-dot"></span><span>maplehollowbloompanels</span></div>
  </section>
</main>
</body>
</html>
```